Healthcare technology company needs website design

We need a logo for a new company based in the U.S. We develop software to assist consumers identifying lowest cost healthcare coverage methods, including insurance, discount cards, and cash options. We would like to see designs that use multiple shades of green with the optional addition of other complimentary colors. The final design should communicate a unique blend of saving money while receiving the healthcare you need.
Need the following pages/sections: Homepage, Solutions, About Us, Contact
Competitors: www.velorimed.example; www.qzplo.example

Target Market(s)

Businesses

Industry/Entity Type

Healthcare

Coding

Coded - Design and coding required

Number of Pages Required

4 page

Colors
0054AA
0677BA
7BADD7
CADEEF
E8F1F8
00AB8E
00BBA5
67D7C9
C6EFE9
E9F9F6

Requirements
Must have
• Matching color theme with logo
Nice to have
• Animated background

```html
<!DOCTYPE html>
<html lang="en">
<head>
<meta charset="utf-8">
<title>Fernleaf Health</title>
<link href="https://fonts.googleapis.com/css2?family=Montserrat:wght@400;500;600;700;800&family=Open+Sans:wght@400;600&display=swap" rel="stylesheet">
<style>
:root{
  --green:#19a34a;
  --green-dark:#0c7a3a;
  --green-deep:#0a5e36;
  --teal:#00ab8e;
  --blue:#0677ba;
  --blue-dark:#0054aa;
  --ink:#1d2b25;
  --grey:#5f6b66;
  --white:#ffffff;
  --mint:#e9f9f6;
}
*{margin:0;padding:0;box-sizing:border-box}
html,body{width:1200px;height:3204px;overflow:hidden;background:var(--white)}
body{position:relative;font-family:"Open Sans",Arial,sans-serif;color:var(--ink)}
.abs{position:absolute}
h1,h2,h3,.brand,.nav,.btn{font-family:"Montserrat",Arial,sans-serif}

/* header */
.site-header{left:0;top:0;width:1200px;height:100px;background:var(--white);z-index:5}
.brand{display:flex;align-items:center;gap:12px;font-weight:800;color:var(--green);font-size:26px;letter-spacing:1px}
.brand .dot{width:34px;height:34px;border-radius:50%;background:var(--green)}
.site-header .brand{left:110px;top:30px}
.nav{left:500px;top:34px;display:flex;gap:56px;font-size:15px;font-weight:600;color:var(--ink);align-items:center}
.nav .active{color:var(--green)}
.nav .nav-contact{background:var(--blue);color:var(--white);padding:9px 32px;border-radius:20px;margin-left:20px}

/* buttons */
.btn{display:inline-block;font-size:13px;font-weight:700;letter-spacing:.5px;padding:11px 26px;border-radius:24px;border:2px solid var(--green);color:var(--green);background:transparent}
.btn.light{border-color:var(--white);color:var(--white)}
.btn::after{content:" ›"}

/* hero */
.hero{left:0;top:100px;width:1200px;height:570px;overflow:hidden}
.hero-title{left:120px;top:236px;color:var(--white);font-size:42px;line-height:50px;font-weight:500}
.hero-title b{font-weight:800}
.hero .btn{left:120px;top:380px}

/* about */
.about-mark{left:110px;top:760px;width:420px;height:420px;border-radius:50%;background:radial-gradient(circle at 40% 40%,#c6efe9,#e9f9f6 70%);display:flex;align-items:center;justify-content:center}
.about-mark .brand{font-size:30px}
h2.section{font-size:34px;line-height:40px;font-weight:800;color:var(--green-dark)}
h2.section span{font-weight:500;color:var(--green)}
.rule{width:60px;height:4px;background:var(--blue)}
.copy{font-size:15px;line-height:24px;color:var(--grey)}

/* solution */
.solution-title{left:0;width:1200px;top:1300px;text-align:center;color:var(--white);font-size:36px;font-weight:500;font-family:"Montserrat",Arial,sans-serif}
.solution-title b{font-weight:800}
.solution-rule{left:570px;top:1350px;width:60px;height:4px;background:var(--white)}
.card{border-radius:50%;border:3px solid var(--white);display:flex;flex-direction:column;align-items:center;justify-content:center;text-align:center;color:var(--white);padding:0 40px}
.card h3{font-size:17px;font-weight:700;margin:16px 0 10px}
.card p{font-size:12px;line-height:18px}
.card.featured{background:var(--green);border-width:6px}
.card .btn{margin-top:16px;font-size:11px;padding:7px 18px;border-color:var(--white);color:var(--white)}

/* why */
.why-photo{left:520px;top:1820px;width:680px;height:560px}

/* contact */
.contact-title{left:140px;top:2480px;font-size:36px;font-weight:800;color:var(--white);font-family:"Montserrat",Arial,sans-serif}
.contact-title span{font-weight:500}
.contact-info{left:140px;top:2560px;color:var(--white);font-size:15px;line-height:24px;width:400px}
.contact-info h3{font-size:17px;font-weight:700;margin-bottom:20px}
.contact-info .row{display:flex;gap:16px;align-items:flex-start;margin-bottom:18px}
.contact-form{left:580px;top:2460px;width:500px;height:390px;background:var(--green-deep);padding:36px 50px}
.field{color:var(--white);font-size:13px;padding-bottom:10px;border-bottom:1px solid rgba(255,255,255,.6);margin-bottom:26px}
.field.tall{height:80px}
.contact-form .submit{background:var(--green);color:var(--white);border-color:var(--green);margin-left:0;font-size:12px}
.contact-form .submit::after{content:""}

/* footer */
.site-footer{left:0;top:2980px;width:1200px;height:224px;background:var(--white);text-align:center}
.site-footer .brand{left:0;width:1200px;justify-content:center;top:4px}
.footer-nav{left:0;width:1200px;top:80px;display:flex;justify-content:center;gap:140px;font-size:13px;font-weight:600;font-family:"Montserrat",Arial,sans-serif}
.legal{left:0;width:1200px;top:118px;font-size:12px;color:var(--grey)}
.social{left:0;width:1200px;top:150px;display:flex;justify-content:center;gap:8px}
.social span{width:26px;height:26px;border-radius:50%;background:var(--green-dark)}
</style>
</head>
<body>

<header class="site-header abs">
  <div class="brand abs"><span class="dot"></span>FERNLEAF HEALTH</div>
  <nav class="nav abs">
    <span class="active">HOME</span><span>SOLUTIONS</span><span>ABOUT US</span><span class="nav-contact">CONTACT</span>
  </nav>
</header>

<section class="hero abs">
  <svg width="1200" height="570" class="abs" style="left:0;top:0">
    <defs>
      <linearGradient id="heroBg" x1="0" y1="0" x2="1" y2="1">
        <stop offset="0" stop-color="#16b04a"/><stop offset=".55" stop-color="#0d8a52"/><stop offset="1" stop-color="#0a5fa0"/>
      </linearGradient>
      <radialGradient id="heroArt" cx=".5" cy=".5" r=".6">
        <stop offset="0" stop-color="#4fd1b8"/><stop offset="1" stop-color="#0b6f88"/>
      </radialGradient>
    </defs>
    <rect width="1200" height="570" fill="url(#heroBg)"/>
    <path d="M520 0 H1200 V570 H760 C600 570 520 480 520 360 Z" fill="url(#heroArt)" role="img" aria-label="Digital healthcare technology illustration with glowing medical icons"/>
  </svg>
  <h1 class="hero-title abs">TECHNOLOGIES<br><b>THAT ARE CHANGING<br>FUTURE OF HEALTHCARE</b></h1>
  <span class="btn light abs">LEARN MORE</span>
</section>

<div class="about-mark abs"><div class="brand"><span class="dot"></span>FERNLEAF</div></div>
<h2 class="section abs" style="left:580px;top:780px">ABOUT FERNLEAF<br><span>HEALTH</span></h2>
<div class="rule abs" style="left:580px;top:870px"></div>
<p class="copy abs" style="left:580px;top:890px;width:500px">Lorem ipsum dolor sit amet, consectetur adipiscing elit, sed do eiusmod tempor incididunt ut labore et dolore magna aliqua. Ut enim ad minim veniam, quis nostrud exercitation ullamco laboris nisi ut aliquip quis nostrud exercitation ullamco.</p>
<p class="copy abs" style="left:580px;top:1010px;width:500px">Duis aute irure dolor in reprehenderit in voluptate velit esse cillum dolore eu fugiat nulla pariatur.</p>
<span class="btn abs" style="left:580px;top:1090px">LEARN MORE</span>

<svg width="1200" height="660" class="abs" style="left:0;top:1180px">
  <defs>
    <linearGradient id="solBg" x1="0" y1="0" x2="1" y2="0">
      <stop offset="0" stop-color="#0e8c5a"/><stop offset=".5" stop-color="#0b7a7e"/><stop offset="1" stop-color="#0a58a6"/>
    </linearGradient>
  </defs>
  <path d="M0 60 C300 0 700 110 1200 20 V600 C800 660 400 560 0 640 Z" fill="url(#solBg)"/>
</svg>
<h2 class="solution-title abs"><b>OUR</b> SOLUTION</h2>
<div class="solution-rule abs"></div>
<div class="card abs" style="left:140px;top:1390px;width:300px;height:300px">
  <svg width="40" height="40" viewBox="0 0 40 40" fill="none" stroke="#fff" stroke-width="2"><rect x="6" y="4" width="28" height="32" rx="2"/><path d="M12 14h16M12 20h16M12 26h10"/></svg>
  <h3>DEVLOP SOFTWARE</h3><p>Lorem ipsum dolor sit amet, consectetur adipiscing elit, sed do eiusmod tempor incididunt ut labore et dolore magna</p>
</div>
<div class="card featured abs" style="left:440px;top:1370px;width:330px;height:330px">
  <svg width="40" height="40" viewBox="0 0 40 40" fill="none" stroke="#fff" stroke-width="2"><rect x="4" y="8" width="32" height="22" rx="2"/><path d="M14 36h12M20 30v6M10 20l6-5 6 5 8-7"/></svg>
  <h3>SED UT PERSPICIATIS</h3><p>Lorem ipsum dolor sit amet, consectetur adipiscing elit, sed do eiusmod tempor incidid</p>
  <span class="btn">LEARN MORE</span>
</div>
<div class="card abs" style="left:760px;top:1390px;width:300px;height:300px">
  <svg width="40" height="40" viewBox="0 0 40 40" fill="none" stroke="#fff" stroke-width="2"><circle cx="20" cy="20" r="6"/><circle cx="8" cy="8" r="3"/><circle cx="32" cy="8" r="3"/><circle cx="8" cy="32" r="3"/><circle cx="32" cy="32" r="3"/><path d="M10 10l6 6M30 10l-6 6M10 30l6-6M30 30l-6-6"/></svg>
  <h3>NEQUE PORRO QUIS</h3><p>Lorem ipsum dolor sit amet, consectetur adipiscing elit, sed do eiusmod tempor incididunt ut labore et dolore magna</p>
</div>

<div class="why-photo abs" role="img" aria-label="Photo of a doctor showing a tablet to an elderly patient in a clinic" style="background:linear-gradient(135deg,#dfe6ea,#b9c7cf 60%,#8fa3ae)"></div>
<h2 class="section abs" style="left:140px;top:1960px">WHY CHOOSE FERNLEAF<br><span>HEALTH</span></h2>
<div class="rule abs" style="left:140px;top:2045px"></div>
<p class="copy abs" style="left:140px;top:2060px;width:440px">Lorem ipsum dolor sit amet, consectetur adipiscing elit, sed do eiusmod tempor incididunt ut labore et dolore magna aliqua. Ut enim ad minim veniam, quis nostrud exercitation ullamco laboris nisi ut aliquip.</p>
<span class="btn abs" style="left:140px;top:2180px">LEARN MORE</span>

<svg width="1200" height="700" class="abs" style="left:0;top:2300px">
  <defs>
    <linearGradient id="conBg" x1="0" y1="0" x2="0" y2="1">
      <stop offset="0" stop-color="#13b35c"/><stop offset="1" stop-color="#0a8a4e"/>
    </linearGradient>
  </defs>
  <path d="M0 80 C400 20 800 60 1200 0 V700 H0 Z" fill="url(#conBg)"/>
</svg>
<h2 class="contact-title abs">CONTACT <span>US</span></h2>
<div class="contact-info abs">
  <h3>FERNLEAF HEALTH</h3>
  <div class="row">
    <svg width="22" height="22" viewBox="0 0 24 24" fill="#fff"><path d="M6.6 10.8a15 15 0 006.6 6.6l2.2-2.2a1 1 0 011-.25 11 11 0 003.6.6 1 1 0 011 1V20a1 1 0 01-1 1A17 17 0 013 4a1 1 0 011-1h3.5a1 1 0 011 1 11 11 0 00.6 3.6 1 1 0 01-.25 1z"/></svg>
    <span>Suite 40, 18 Marlow Lane,<br>Easthill, EH2 4QT</span>
  </div>
  <div class="row">
    <svg width="22" height="22" viewBox="0 0 24 24" fill="none" stroke="#fff" stroke-width="2"><rect x="3" y="5" width="18" height="14" rx="2"/><path d="M3 7l9 6 9-6"/></svg>
    <span>info@fernleaf.example</span>
  </div>
  <span class="btn light" style="margin-top:10px">GET IN TOUCH</span>
</div>
<form class="contact-form abs">
  <div class="field">Your Name</div>
  <div class="field">E-mail address</div>
  <div class="field">Phone</div>
  <div class="field tall">Message</div>
  <span class="btn submit">SUBMIT NOW</span>
</form>

<footer class="site-footer abs">
  <div class="brand abs"><span class="dot"></span>FERNLEAF HEALTH</div>
  <nav class="footer-nav abs"><span>HOME</span><span>SOLUTIONS</span><span>ABOUT US</span><span>RESOURCES</span><span>CONTACT</span></nav>
  <p class="legal abs">© 2022 Company Name | All Rights Reserved</p>
  <div class="social abs"><span></span><span></span><span></span><span></span></div>
</footer>

</body>
</html>
```